Create look and feel for existing Web Page

Update Web Page

We have a website at http://www.usekivra.com/index-web.html. It is a single page html site, with a custom signup form. We also have a quill bay plugin at the bottom of the page. We'd like to redesign the look and feel of the entire site. We sell software to eye doctors. Also called optometrists, our software tool makes it easy for doctors to manage patients, bill, and document patient encounters. I have included our logos below.

We are looking for a new design preferably in HTML 5, CSS etc. The fields on the form on this page: http://www.usekivra.com/index-web.html

You can get screen shots of our software application at this site: http://staging.usekivra.com
username: test@samplevora.com
password: password

```html
<!DOCTYPE html>
<html lang="en">
<head>
<meta charset="utf-8">
<title>Tarvio — The Practice Operating System</title>
<link href="https://fonts.googleapis.com/css2?family=Fira+Sans:wght@300;400;500;600&family=Montserrat:wght@500;600;700;800&display=swap" rel="stylesheet">
<style>
:root{
  --orange:#ff7f11;
  --orange-deep:#ff6a00;
  --orange-light:#ffa218;
  --ink:#2f3340;
  --slate:#3d4150;
  --muted:#8c8f98;
  --line:#ececec;
  --soft:#f7f7f7;
  --blue:#0b9be3;
  --white:#ffffff;
}
*{box-sizing:border-box;margin:0;padding:0}
html,body{width:1200px;height:2812px;overflow:hidden}
body{position:relative;font-family:"Fira Sans",Arial,sans-serif;color:var(--ink);background:var(--white)}
.abs{position:absolute}
.wordmark{font-family:"Fira Sans",Arial,sans-serif;font-weight:400;color:var(--orange);letter-spacing:1px}

/* header */
.site-header{left:0;top:0;width:1200px;height:75px;background:var(--white);box-shadow:0 1px 4px rgba(0,0,0,.08);z-index:2}
.site-header .wordmark{left:160px;top:12px;font-size:40px}
.main-nav{left:504px;top:28px;display:flex;gap:40px;font-size:12px;font-weight:500;letter-spacing:.3px}
.main-nav a{color:var(--ink);text-decoration:none;padding-bottom:8px}
.main-nav a.active{border-bottom:2px solid var(--orange)}
.auth{left:908px;top:22px;display:flex;align-items:center;gap:10px;font-size:12px;color:var(--muted)}
.btn-signup{border:1.5px solid var(--orange);color:var(--orange);padding:7px 16px;font-weight:500}
.auth .login{color:var(--orange)}

/* hero */
.hero{left:0;top:75px;width:1200px;height:525px;background:linear-gradient(120deg,#eceef0 0%,#f6f7f8 45%,#e8eaec 100%)}
.hero-copy{left:161px;top:145px;width:300px}
.hero-kicker{font-size:14px;color:var(--ink)}
.hero-title{font-family:Montserrat,Arial,sans-serif;font-weight:700;color:var(--orange);font-size:38px;margin-top:6px}
.hero-sub{font-family:Montserrat,Arial,sans-serif;font-weight:600;font-size:16px;margin-top:4px}
.hero-text{font-size:11.5px;line-height:20px;color:var(--muted);margin-top:14px}
.btn-hero{display:inline-block;margin-top:18px;background:var(--orange);color:var(--white);font-size:11px;font-weight:500;padding:9px 20px}
.app-screen{left:510px;top:178px;width:482px;height:314px;border-radius:14px 14px 0 0;background:linear-gradient(180deg,#2a2c33 0%,#3a3d45 100%)}
.app-base{left:461px;top:492px;width:578px;height:14px;border-radius:0 0 8px 8px;background:linear-gradient(180deg,#d9dadc,#b9bbbe)}

/* features */
.features-head{left:0;top:665px;width:1200px;text-align:center}
.section-title{font-family:Montserrat,Arial,sans-serif;font-weight:500;font-size:28px;color:var(--ink)}
.features-head p{font-size:12.5px;color:var(--muted);margin-top:6px}
.tags{display:flex;justify-content:center;gap:16px;margin-top:18px;font-size:12px;letter-spacing:.4px;font-weight:400}
.tags span.dot{width:5px;height:5px;border-radius:50%;background:var(--orange);align-self:center}
.feature-card{width:201px;height:199px;border:1px solid var(--line);border-radius:3px;padding:20px 20px;background:var(--white)}
.feature-card.raised{box-shadow:0 6px 18px rgba(0,0,0,.1);border-color:transparent}
.feature-card svg{width:42px;height:42px;display:block}
.feature-card h3{font-size:16px;font-weight:500;margin-top:16px}
.feature-card p{font-size:10.3px;line-height:18px;color:var(--muted);margin-top:8px}

/* pricing */
.pricing{left:0;top:1320px;width:1200px;height:649px;background:var(--soft)}
.pricing .section-title{position:absolute;left:0;top:54px;width:1200px;text-align:center}
.price-card{top:135px;width:276px;height:356px;border-radius:4px;color:var(--white);text-align:center;padding-top:34px}
.price-card.basic{left:311px;background:var(--orange)}
.price-card.addon{left:611px;background:var(--slate)}
.price-card h4{font-family:Montserrat,Arial,sans-serif;font-weight:600;font-size:15px;letter-spacing:.3px}
.amount{font-family:Montserrat,Arial,sans-serif;font-weight:700;font-size:72px;margin-top:14px;line-height:1}
.amount sup{font-size:30px;vertical-align:top;position:relative;top:6px}
.amount .slash{font-weight:300}
.amount small{font-size:15px;font-weight:500}
.price-card .note{font-size:12.5px;margin-top:40px;opacity:.9}
.price-card .aside{font-size:10.5px;margin-top:6px;opacity:.8}
.btn-buy{position:absolute;left:50%;transform:translateX(-50%);top:280px;font-size:12px;padding:9px 22px;color:var(--white)}
.basic .btn-buy{background:#c9590a}
.addon .btn-buy{background:#2b2e38}
.pricing-foot{top:540px;left:190px;width:820px;text-align:center;font-size:15px;line-height:28px;color:#5b5e66}

/* lease band */
.lease{left:0;top:1969px;width:1200px;height:319px;background:var(--blue);color:var(--white)}
.lease-col{top:58px;width:280px}
.lease-col.left{left:256px;text-align:right}
.lease-col.right{left:664px}
.lease-col h3{font-family:"Fira Sans",Arial,sans-serif;font-weight:500;font-size:18px;line-height:26px}
.lease-col p{font-size:10.5px;line-height:19px;margin-top:14px;opacity:.92}
.lease-divider{left:600px;top:58px;width:1px;height:140px;background:rgba(255,255,255,.3)}
.btn-join{left:536px;top:217px;width:126px;height:40px;background:var(--slate);color:var(--white);font-size:11px;font-weight:500;display:flex;align-items:center;justify-content:center}

/* waitlist */
.waitlist{left:0;top:2288px;width:1200px;height:524px;background:linear-gradient(100deg,var(--orange-deep) 0%,var(--orange) 50%,var(--orange-light) 100%);color:var(--white)}
.waitlist-copy{left:161px;top:68px;width:340px}
.waitlist-copy .kicker{font-size:12px;font-style:italic;letter-spacing:.3px}
.waitlist-copy h2{font-family:Montserrat,Arial,sans-serif;font-weight:800;font-size:27px;line-height:38px;margin-top:10px}
.waitlist-copy p{font-size:11.5px;line-height:21px;margin-top:14px}
.btn-contact{left:161px;top:251px;width:128px;height:35px;background:var(--slate);color:var(--white);font-size:11px;font-weight:500;display:flex;align-items:center;justify-content:center;box-shadow:0 8px 16px rgba(0,0,0,.2)}
.signup-form{left:686px;top:74px;width:351px}
.field{height:37px;margin-bottom:12px;background:rgba(130,60,0,.35);font-size:10.5px;padding:11px 14px;color:rgba(255,255,255,.9)}
.btn-submit{height:38px;margin-top:4px;background:var(--orange);font-size:12px;font-weight:500;display:flex;align-items:center;justify-content:center;box-shadow:0 6px 14px rgba(180,70,0,.35)}
.site-footer .wordmark{left:160px;top:433px;font-size:40px;color:var(--white)}
.social{left:338px;top:460px;display:flex;gap:12px}
.social span{width:9px;height:9px;border-radius:50%;background:var(--white)}
.copyright{left:690px;top:456px;width:347px;text-align:right;font-size:10px}
</style>
</head>
<body>

<header class="site-header abs">
  <div class="wordmark abs">tarvio</div>
  <nav class="main-nav abs">
    <a class="active" href="#">HOME</a>
    <a href="#">PRODUCTS</a>
    <a href="#">PRICING</a>
  </nav>
  <div class="auth abs"><span class="btn-signup">Sign Up</span><span>or</span><span class="login">Log in</span></div>
</header>

<section class="hero abs" role="img" aria-label="Soft grey photo of an eye exam room behind the hero">
  <div class="hero-copy abs">
    <div class="hero-kicker">Tired of all the administrative work?</div>
    <h1 class="hero-title">Meet Tarvio</h1>
    <div class="hero-sub">The Practice Operating System</div>
    <p class="hero-text">Tarvio is your office operating system. Automate your painful tasks, keep track of your books, and live a little. Start with a FREE charting tool and add more products as you grow.</p>
    <span class="btn-hero">Get the charting tool for free</span>
  </div>
</section>
<div class="app-screen abs" role="img" aria-label="Laptop showing the Tarvio schedule screen"></div>
<div class="app-base abs"></div>

<section class="features-head abs">
  <h2 class="section-title">What can you do with tarvio ?</h2>
  <p>What if running your lease was as simple as a tarvio patient?</p>
  <div class="tags"><span>SIMPLE</span><span class="dot"></span><span>FULLY AUTOMATED</span><span class="dot"></span><span>PROFITABLE</span></div>
</section>

<div class="feature-card raised abs" style="left:161px;top:834px">
  <svg viewBox="0 0 42 42" fill="none" stroke="var(--orange)" stroke-width="2"><rect x="4" y="8" width="30" height="24" rx="2"/><line x1="4" y1="15" x2="34" y2="15"/><rect x="12" y="20" width="14" height="8" fill="var(--orange)" stroke="none" opacity=".5"/></svg>
  <h3>Online Booking</h3>
  <p>Lorem ipsum dolor sit amet, consectetur adipisicing elit, sed do eiusmod tempor incididunt ut labore et dolore magna</p>
</div>
<div class="feature-card abs" style="left:386px;top:834px">
  <svg viewBox="0 0 42 42" fill="none" stroke="var(--orange)" stroke-width="2"><path d="M10 30V19a10 10 0 0 1 20 0v11z"/><line x1="6" y1="30" x2="34" y2="30"/><path d="M17 34a3 3 0 0 0 6 0"/><line x1="34" y1="4" x2="34" y2="12"/><line x1="30" y1="8" x2="38" y2="8"/></svg>
  <h3>Reminders</h3>
  <p>Lorem ipsum dolor sit amet, consectetur adipisicing elit, sed do eiusmod tempor incididunt ut labore et dolore magna</p>
</div>
<div class="feature-card abs" style="left:611px;top:834px">
  <svg viewBox="0 0 42 42" fill="none" stroke="var(--orange)" stroke-width="2"><rect x="4" y="5" width="34" height="30"/><line x1="9" y1="12" x2="33" y2="12"/><line x1="9" y1="18" x2="33" y2="18"/><line x1="9" y1="24" x2="33" y2="24"/><line x1="9" y1="30" x2="24" y2="30"/></svg>
  <h3>Automated Forms</h3>
  <p>Lorem ipsum dolor sit amet, consectetur adipisicing elit, sed do eiusmod tempor incididunt ut labore et dolore magna</p>
</div>
<div class="feature-card abs" style="left:836px;top:834px">
  <svg viewBox="0 0 42 42" fill="none" stroke="var(--orange)" stroke-width="2"><circle cx="21" cy="8" r="5"/><path d="M18.5 8l2 2 3-3.5"/><circle cx="10" cy="22" r="3.5"/><circle cx="21" cy="22" r="3.5"/><circle cx="32" cy="22" r="3.5"/><path d="M4 34a6 6 0 0 1 12 0M15 34a6 6 0 0 1 12 0M26 34a6 6 0 0 1 12 0"/></svg>
  <h3>Eligibility</h3>
  <p>Lorem ipsum dolor sit amet, consectetur adipisicing elit, sed do eiusmod tempor incididunt ut labore et dolore magna</p>
</div>
<div class="feature-card abs" style="left:161px;top:1059px">
  <svg viewBox="0 0 42 42" fill="none" stroke="var(--orange)" stroke-width="2"><path d="M8 8l26 26-4 4L4 12z"/><line x1="12" y1="12" x2="8" y2="16"/><line x1="30" y1="30" x2="34" y2="34"/></svg>
  <h3>Charting</h3>
  <p>Lorem ipsum dolor sit amet, consectetur adipisicing elit, sed do eiusmod tempor incididunt ut labore et dolore magna</p>
</div>
<div class="feature-card abs" style="left:386px;top:1059px">
  <svg viewBox="0 0 42 42" fill="none" stroke="var(--orange)" stroke-width="2"><rect x="6" y="4" width="30" height="22" rx="2"/><rect x="12" y="14" width="18" height="22"/><line x1="16" y1="20" x2="26" y2="20"/><line x1="16" y1="26" x2="26" y2="26"/></svg>
  <h3>Auto Billing</h3>
  <p>Lorem ipsum dolor sit amet, consectetur adipisicing elit, sed do eiusmod tempor incididunt ut labore et dolore magna</p>
</div>
<div class="feature-card abs" style="left:611px;top:1059px">
  <svg viewBox="0 0 42 42" fill="none" stroke="var(--orange)" stroke-width="2"><path d="M12 24V12l6-8 2 2-2 6h10v12z"/><rect x="6" y="12" width="6" height="12"/><path d="M7 36l2-4 2 4M19 36l2-4 2 4M31 36l2-4 2 4"/></svg>
  <h3>Reviews</h3>
  <p>Lorem ipsum dolor sit amet, consectetur adipisicing elit, sed do eiusmod tempor incididunt ut labore et dolore magna</p>
</div>
<div class="feature-card abs" style="left:836px;top:1059px">
  <svg viewBox="0 0 42 42" fill="none" stroke="var(--orange)" stroke-width="2"><path d="M34 21a13 13 0 1 1-4-9.4"/><path d="M31 5v7h-7"/><path d="M16 15c0 6 5 11 11 11l2-3-4-2-2 2c-2-1-4-3-5-5l2-2-2-4z"/></svg>
  <h3>Recall</h3>
  <p>Lorem ipsum dolor sit amet, consectetur adipisicing elit, sed do eiusmod tempor incididunt ut labore et dolore magna</p>
</div>

<section class="pricing abs">
  <h2 class="section-title">Pricing</h2>
  <div class="price-card basic abs">
    <h4>STARTING AT</h4>
    <div class="amount"><sup>$</sup>49<span class="slash">/</span><small> month</small></div>
    <p class="note">Gets you started with Charting</p>
    <span class="btn-buy">Buy Now</span>
  </div>
  <div class="price-card addon abs">
    <h4>STARTING AT</h4>
    <div class="amount"><sup>$</sup>99<span class="slash">/</span><small> month</small></div>
    <p class="note" style="margin-top:34px">Per additional feature</p>
    <p class="aside">( no worries just turn off if you don't love it )</p>
    <span class="btn-buy">Buy Now</span>
  </div>
  <p class="pricing-foot abs">You start with charting at $49/mon and then add features as you need them. What other software allows you to only pay for what you want?</p>
</section>

<section class="lease abs">
  <div class="lease-col left abs">
    <h3>Designed for Lease doctors</h3>
    <p>Lease doctors were frustrated with the administration associated with running a lease practice so instead of complaining they created a system to do it for them.</p>
  </div>
  <div class="lease-divider abs"></div>
  <div class="lease-col right abs">
    <h3>Just you and Tarvio can run your lease practice</h3>
    <p>No really, you need to check Tarvio out. If you want, your lease can be completely automated. No more late nights and HR frustrations</p>
  </div>
  <div class="btn-join abs">Join Us Today!</div>
</section>

<section class="waitlist abs">
  <div class="waitlist-copy abs">
    <div class="kicker">GET ON THE WAITLIST</div>
    <h2>Get Started With a Charting Tool</h2>
    <p>Become part of a club that wants to change the way we practice, so we can have a life outside of the office.</p>
  </div>
  <div class="btn-contact abs">Contact</div>
  <form class="signup-form abs">
    <div class="field">Full Name</div>
    <div class="field">Email</div>
    <div class="field">Cell Phone</div>
    <div class="field">Office Name</div>
    <div class="field">NPI</div>
    <div class="btn-submit">Get the free charging tool</div>
  </form>
  <footer class="site-footer">
    <div class="wordmark abs">tarvio</div>
    <div class="social abs"><span></span><span></span><span></span><span></span></div>
    <div class="copyright abs">© Tarvio 2020 All rights reserved.</div>
  </footer>
</section>

</body>
</html>
```